Gaphic explaining connectivity of research areas that use DNA analysis

We are a university research group in Perth Western Australia focused on ecology and environment fields. Our work can be explained by three broad areas where its applied - what used to be present ('ancient DNA analysis'), what is present now ('environmental DNA analysis') and what happened in terms of DNA based changes in between ('genomic changes'). To help simply convey this to other researchers and importantly non-science-savvy people we wanted an a eye catching rework of the attached for our website, future presentations, brochures etc. We didn't want it too visually complicated, nor wordy so something akin to the attached with a better look will help . More background on each point can be read on the website under construction here - https://sciweb.halvorne.edu.au/quill-lab/

Target Market(s)

other science researchers in ecology, environment, geology, forensics areas, although ultimately its meant to be a simple way to understand for all people

Font styles to use
Sans Serif

Requirements
Must have
• the three areas indicated
Should not have
• design does not need to follow the colour pallet of the university (ie poo brown and black)

```html
<!DOCTYPE html>
<html lang="en">
<head>
<meta charset="utf-8">
<title>Quill Lab – DNA research pathway</title>
<link href="https://fonts.googleapis.com/css2?family=Lato:wght@700;900&display=swap" rel="stylesheet">
<style>
  :root {
    --navy: #0d4c85;
    --teal: #1a8a89;
    --sky: #3f8fe6;
    --map-teal: #52b3b2;
    --grey: #555555;
    --white: #ffffff;
    --lens: #c3dcf7;
  }
  html, body { margin: 0; padding: 0; overflow: hidden; background: var(--white); }
  .canvas {
    position: relative;
    width: 1184px;
    height: 1200px;
    overflow: hidden;
    background: var(--white);
    font-family: "Lato", sans-serif;
  }
  .brand {
    position: absolute;
    left: 0; width: 1184px; top: 62px;
    text-align: center;
    font-weight: 900;
    font-size: 60px;
    letter-spacing: 2px;
    color: var(--teal);
    margin: 0;
  }
  .pathway { position: absolute; left: 0; top: 0; }
  .icon { position: absolute; }
  .area-title {
    position: absolute;
    margin: 0;
    font-weight: 900;
    font-size: 63px;
    line-height: 1;
    color: var(--navy);
    white-space: nowrap;
  }
  .area-question {
    position: absolute;
    margin: 0;
    font-weight: 700;
    font-size: 32px;
    line-height: 1;
    color: var(--grey);
    white-space: nowrap;
  }
  .centred { transform: translateX(-50%); }
  .region {
    position: absolute;
    left: 317px; top: 650px;
    width: 552px; height: 470px;
    background: var(--map-teal);
    border-radius: 46% 40% 44% 48% / 36% 40% 52% 44%;
  }
  .region-caption {
    position: absolute;
    left: 317px; width: 552px; top: 764px;
    margin: 0;
    text-align: center;
    font-weight: 900;
    font-size: 26px;
    line-height: 34.5px;
    letter-spacing: 0.5px;
    color: var(--white);
  }
</style>
</head>
<body>
<div class="canvas">

  <svg width="0" height="0" style="position:absolute">
    <defs>
      <symbol id="helix" viewBox="0 0 240 240">
        <g transform="rotate(-55 120 120)" fill="none" stroke-linecap="round">
          <g stroke="var(--sky)" stroke-width="5">
            <line x1="45" y1="88" x2="45" y2="152"/>
            <line x1="55" y1="83" x2="55" y2="157"/>
            <line x1="65" y1="83" x2="65" y2="157"/>
            <line x1="75" y1="88" x2="75" y2="152"/>
            <line x1="165" y1="88" x2="165" y2="152"/>
            <line x1="175" y1="83" x2="175" y2="157"/>
            <line x1="185" y1="83" x2="185" y2="157"/>
            <line x1="195" y1="88" x2="195" y2="152"/>
          </g>
          <path d="M-20 120 Q15 30 50 120 T120 120 T190 120 T260 120" stroke="var(--navy)" stroke-width="15"/>
          <path d="M-20 120 Q15 210 50 120 T120 120 T190 120 T260 120" stroke="var(--teal)" stroke-width="15"/>
        </g>
      </symbol>
      <symbol id="clock" viewBox="0 0 80 80">
        <circle cx="40" cy="40" r="34" fill="var(--white)" stroke="var(--navy)" stroke-width="7"/>
        <path d="M36 22 V46 H54" fill="none" stroke="var(--navy)" stroke-width="7" stroke-linecap="square"/>
      </symbol>
      <symbol id="lens" viewBox="0 0 100 100">
        <line x1="62" y1="62" x2="92" y2="92" stroke="var(--navy)" stroke-width="12" stroke-linecap="round"/>
        <circle cx="40" cy="40" r="33" fill="var(--lens)" stroke="var(--navy)" stroke-width="8"/>
      </symbol>
    </defs>
  </svg>

  <h1 class="brand">QUILL LAB</h1>

  <svg class="pathway" width="1184" height="1200" viewBox="0 0 1184 1200" aria-hidden="true">
    <path d="M0 707 H333 V582 H743 V451 H1125" fill="none" stroke="var(--teal)" stroke-width="23"/>
    <polygon points="1118,414 1177,451 1118,486" fill="var(--teal)"/>
  </svg>

  <!-- Environmental DNA -->
  <svg class="icon" style="left:97px; top:303px" width="195" height="200" aria-hidden="true">
    <use href="#helix" x="0" y="0" width="190" height="200"/>
    <use href="#clock" x="100" y="120" width="78" height="78"/>
  </svg>
  <h2 class="area-title" style="left:72px; top:524px">eDNA</h2>
  <p class="area-question" style="left:46px; top:600px">What is present?</p>

  <!-- Ancient DNA -->
  <svg class="icon" style="left:426px; top:181px" width="200" height="200" aria-hidden="true">
    <use href="#helix" x="0" y="0" width="190" height="200"/>
    <use href="#clock" x="116" y="100" width="80" height="80"/>
  </svg>
  <h2 class="area-title centred" style="left:524px; top:401px">aDNA</h2>
  <p class="area-question centred" style="left:524px; top:481px">What used to be present?</p>

  <!-- Genomics -->
  <svg class="icon" style="left:840px; top:55px" width="215" height="195" aria-hidden="true">
    <use href="#helix" x="0" y="0" width="190" height="195"/>
    <use href="#lens" x="112" y="90" width="100" height="100"/>
  </svg>
  <h2 class="area-title centred" style="left:943px; top:273px">Genomics</h2>
  <p class="area-question centred" style="left:943px; top:355px">What happened along the way?</p>

  <div class="region" role="img" aria-label="Map of Australia in teal"></div>
  <p class="region-caption">INSIGHT ON THE<br>FORMATION<br>DISTRIBUTIONAND<br>RESILIENCE<br>OF AUSTRALIAN&nbsp; BIODIVERSITY</p>

</div>
</body>
</html>
```